Card for invoking rights with police

Our criminal defense law firm is seeking proposals for a design for our card intended for clients to carry with them in their car. Upon being pulled over, they would hand this card to the officer.
Text for the back of the card:
"For Law Enforcement:"
"I will comply with lawful orders but respectfully decline any test or other requests without my attorney. I wish to remain silent, do not consent to searches, and request to speak with my attorney now.
The back of the card should prominently feature the text and the firm logo should be secondary.
Front
Must prominently feature contact info: 503-555-0182. Do not include attorney name, email, phone from the example file. This is intended to be generic for the firm and not tied to an individual lawyer.
Included for design reference: current business card, firm logo.
We intend to use trenvo.com to produce the cards.
Updates
The back of the card should prominently display the text regarding invocation of rights. Please title it "For Law Enforcement".
Target Market(s)
People who have been stopped by police
Contact Information for Business Card
see project description
Look and feel

```html
<!DOCTYPE html>
<html lang="en">
<head>
<meta charset="utf-8">
<title>Brennard Law Firm – Rights Card</title>
<link href="https://fonts.googleapis.com/css2?family=Bebas+Neue&family=Montserrat:wght@300;500&display=swap" rel="stylesheet">
<style>
  :root {
    --page-bg: #03284a;
    --card-bg: #0a2f51;
    --ink: #ffffff;
    --ring: #8c8c8c;
    --dot: #ffffff;
  }
  html, body {
    margin: 0;
    padding: 0;
    width: 813px;
    height: 1200px;
    overflow: hidden;
    background: var(--page-bg);
  }
  .canvas {
    position: relative;
    width: 813px;
    height: 1200px;
  }
  .card {
    position: absolute;
    left: 146px;
    width: 520px;
    height: 297px;
    background: var(--card-bg);
    overflow: hidden;
    color: var(--ink);
  }
  .card--front { top: 28px; }
  .card--back { top: 335px; }
  .decor {
    position: absolute;
    inset: 0;
    width: 100%;
    height: 100%;
  }
  .decor .ring { fill: var(--ring); }
  .decor .dot { fill: var(--dot); }

  .brand {
    position: absolute;
    left: 0;
    right: 0;
    display: flex;
    justify-content: center;
    align-items: center;
    gap: 8px;
    font-family: "Montserrat", sans-serif;
    font-weight: 500;
    color: var(--ink);
    letter-spacing: 0.18em;
    white-space: nowrap;
  }
  .brand__mark {
    background: var(--ink);
    flex: none;
  }
  .card--front .brand { top: 27px; font-size: 14px; }
  .card--front .brand__mark { width: 20px; height: 20px; }
  .card--back .brand { top: 240px; font-size: 10px; }
  .card--back .brand__mark { width: 14px; height: 14px; }

  .contact-box {
    position: absolute;
    left: 73px;
    top: 75px;
    width: 370px;
    height: 143px;
    border: 2px solid var(--ink);
    border-radius: 24px;
    text-align: center;
  }
  .contact-box__icon {
    display: block;
    margin: 19px auto 0;
    width: 32px;
    height: 32px;
  }
  .contact-box__icon path { fill: var(--ink); }
  .contact-box__phone {
    margin: 6px 0 0;
    font-family: "Bebas Neue", sans-serif;
    font-size: 66px;
    line-height: 1;
    letter-spacing: 0.01em;
  }
  .website {
    position: absolute;
    left: 0;
    right: 0;
    top: 250px;
    margin: 0;
    text-align: center;
    font-family: "Montserrat", sans-serif;
    font-weight: 500;
    font-size: 12px;
    letter-spacing: 0.62em;
  }

  .notice__title {
    position: absolute;
    left: 0;
    right: 0;
    top: 44px;
    margin: 0;
    text-align: center;
    font-family: "Bebas Neue", sans-serif;
    font-weight: 400;
    font-size: 36px;
    line-height: 1;
    letter-spacing: 0.01em;
  }
  .notice__body {
    position: absolute;
    left: 0;
    right: 0;
    top: 108px;
    margin: 0;
    text-align: center;
    font-family: "Montserrat", sans-serif;
    font-weight: 300;
    font-size: 14.2px;
    line-height: 19px;
  }
</style>
</head>
<body>
<main class="canvas">

  <section class="card card--front" aria-label="Card front">
    <svg class="decor" viewBox="0 0 520 297" aria-hidden="true">
      <circle class="ring" cx="-4" cy="-4" r="95"/>
      <circle class="dot" cx="-4" cy="-4" r="79"/>
      <circle class="ring" cx="534" cy="252" r="56"/>
      <circle class="dot" cx="534" cy="252" r="41"/>
    </svg>

    <div class="brand">
      <span class="brand__mark"></span>
      <span class="brand__name">BRENNARD LAW FIRM</span>
    </div>

    <div class="contact-box">
      <svg class="contact-box__icon" viewBox="0 0 32 32" aria-hidden="true">
        <path d="M16 4c-6 0-11 1.6-13 4-.8 1-.6 3 .3 3.6l3.5 1.6c.9.4 1.9-.1 2.1-1l.5-2.2c2-.6 4.3-.9 6.6-.9s4.6.3 6.6.9l.5 2.2c.2.9 1.2 1.4 2.1 1l3.5-1.6c.9-.6 1.1-2.6.3-3.6C27 5.6 22 4 16 4z"/>
        <path fill-rule="evenodd" d="M11 12h10l1 3 5 6v6c0 1-.7 1.5-1.5 1.5h-19C5.7 28.5 5 28 5 27v-6l5-6 1-3zm5 6.2a3.8 3.8 0 1 0 0 7.6 3.8 3.8 0 0 0 0-7.6zm0 2a1.8 1.8 0 1 1 0 3.6 1.8 1.8 0 0 1 0-3.6z"/>
      </svg>
      <p class="contact-box__phone">503-555-0182</p>
    </div>

    <p class="website">www.brennardlawfirm.com</p>
  </section>

  <section class="card card--back notice" aria-label="Card back">
    <svg class="decor" viewBox="0 0 520 297" aria-hidden="true">
      <circle class="ring" cx="538" cy="42" r="51"/>
      <circle class="dot" cx="538" cy="42" r="35"/>
      <circle class="ring" cx="0" cy="300" r="85"/>
      <circle class="dot" cx="0" cy="300" r="67"/>
    </svg>

    <h1 class="notice__title">For Law Enforcement</h1>
    <p class="notice__body">
      I will comply with lawful orders but respectfully decline<br>
      any test or other requests without my attorney.<br>
      I wish to remain silent, do not consent to searches,<br>
      and request to speak with my attorney now.
    </p>

    <div class="brand">
      <span class="brand__mark"></span>
      <span class="brand__name">BRENNARD LAW FIRM</span>
    </div>
  </section>

</main>
</body>
</html>
```